Need Professional, Modern, Clean Newsletter Templates for High End Real Estate Agents in Orange Coun

I need a newsletter for realtors who specialize in high-end home sales for Orange County, California. Please see the attached draft of the newsletter we have in mind. Please note the logo at the top and the beach imagery and please use these and complementary fonts, colors and themes when creating your design. These particular realtors focus on very high-end clients with a specialization on ocean front properties. I WANT YOU TO PLEASE USE THE HEADER FROM MY ATTACHMENT IN YOUR NEWSLETTER. THIS NEWSLETTER IS INTENDED TO BE SENT OUT VIA EMAIL ONLY, NOT PRINT.

The idea behind the newsletter is that it will cover four broad categories. We will have a content creator who will pull content each week, however we need a nice looking template that can support their content. These are the four categories :

1) Market Data - this will pull graphs and information that the realtors receive, directly from the MLS (home listing site). Most of this will be in graph or table form, so we need a nice way to support that.

2.) Featured Listings - this will show the featured homes they have for sale at any given time. This section of the template should have a place to put pictures of the home with supporting text.

3.) News you can use - links to videos and articles relevant to the real estate industry and in the area.

4.) Upcoming OC Events - list of upcoming events in the area.

I feel like I need to post this update in case there was some confusion in my contest brief.

I DO NOT want a new logo or header design. What I am looking for is a newsletter to support the header and logo I already have, and for a nice template which includes each of the four sections I described in my brief. I would like you to think about each of the four sections and design them accordingly. There needs to be a good section for graphs (market data), for videos, for featured listings (pictures of homes with supporting descriptive text) and upcoming events (maybe supported by a calendar and text sections to describe the event, etc.)

This newsletter will be sent out as email only. Your entries should be made as .pdf or as a word document. Thanks.

Target Market(s)

High end real estate buyers and sellers, with a focus on ocean front property.

Industry/Entity Type

Real Estate

Colors
33a6d7
00a990
86cae6

Requirements
Must have
• You MUST include the header photo from the .png attachment I included. "Kestwin Shoreline Homes - Your Coastal Closers."

```html
<!DOCTYPE html>
<html lang="en">
<head>
<meta charset="utf-8">
<title>Kestwin Shoreline Homes – January 2014 Newsletter</title>
<link href="https://fonts.googleapis.com/css2?family=Figtree:wght@400;500;600;700&family=Oswald:wght@300&display=swap" rel="stylesheet">
<style>
:root{
  --page:#eef0f2;
  --paper:#ffffff;
  --ink:#333537;
  --muted:#8b9095;
  --rule:#dcdfe2;
  --teal:#00a990;
  --blue:#33a6d7;
  --sky:#86cae6;
  --quick:#3db3da;
  --dark:#2b2c2d;
  --panel:#eceeef;
  --cell:#eef0f1;
  --cell-line:#d6d9dc;
  --bar:#f0474b;
  --bar-top:#2fa98f;
  --band:#e3e6e8;
  --footer-text:#b9bcbf;
}
*{box-sizing:border-box;margin:0;padding:0}
html,body{width:1200px;height:3922px;overflow:hidden}
body{background:var(--page);font-family:"Figtree",Arial,sans-serif;color:var(--ink);position:relative}
.abs{position:absolute}

.sent-date{right:40px;top:24px;font-size:15px;color:#3a3c3e}
.sent-toggle{left:977px;top:70px;width:16px;height:10px}

.sheet{left:186px;top:105px;width:828px;height:3667px;background:var(--paper)}

.hero{left:199px;top:112px;width:802px;height:333px;
  background:linear-gradient(180deg,#bfe3f3 0%,#79c1e2 22%,#2f9ccb 44%,#39b7c8 60%,#7fd0cf 74%,#dfe9e2 88%,#e9e3d3 100%)}
.brand-box{left:235px;top:214px;width:215px;height:139px;background:rgba(255,255,255,.92);
  display:flex;align-items:center;padding:0 20px}
.brand-name{font-size:27px;font-weight:600;line-height:1.15;color:var(--blue);letter-spacing:.5px}
.tagline{left:560px;width:415px;top:260px;text-align:right;white-space:nowrap;font-family:"Oswald","Arial Narrow",sans-serif;font-weight:300;font-size:36px;line-height:44px;color:#fff;letter-spacing:2.5px}

.main-nav{left:199px;top:450px;width:802px;height:62px;background:var(--dark);display:flex;align-items:center;justify-content:center}
.main-nav span{color:#e9e9e9;font-size:15px;font-weight:500;letter-spacing:1px;padding:0 34px;border-left:1px solid #4a4b4c;line-height:26px}
.main-nav span:first-child{border-left:0}

.section-title{font-size:23px;font-weight:600;color:var(--ink)}
.rule{height:2px;background:var(--rule)}
.body-copy{font-size:18px;line-height:31px;color:var(--muted)}

.welcome-title{left:227px;top:555px}
.welcome-rule{left:227px;top:605px;width:746px}
.welcome-copy{left:227px;top:619px;width:746px}

.letter{left:199px;top:763px;width:802px;height:322px;background:var(--teal)}
.portrait{left:217px;top:784px;width:214px;height:282px;border:9px solid #fff;
  background:linear-gradient(160deg,#4d3a2e 0%,#7a6656 45%,#a39584 70%,#5e5148 100%)}
.letter-title{left:468px;top:792px;font-size:27px;font-weight:700;color:#fff;letter-spacing:.5px}
.letter-copy{left:468px;top:840px;width:510px;font-size:17px;line-height:31px;color:#fff;font-weight:500}
.letter-name{left:468px;top:1000px;font-size:21px;font-weight:700;color:#fff}
.letter-mail{left:468px;top:1036px;font-size:17px;font-weight:600;color:#fff}

.links-title{left:227px;top:1142px;font-size:22px;font-weight:500}
.links-rule{left:227px;top:1191px;width:746px}

.quick-links{left:199px;top:1221px;width:802px;height:259px;background:var(--quick);display:flex}
.quick-link{flex:1;display:flex;flex-direction:column;align-items:center;padding-top:50px;border-left:1px solid rgba(255,255,255,.35);margin:22px 0}
.quick-link:first-child{border-left:0}
.quick-icon{width:88px;height:88px;border-radius:50%;background:#fff;display:flex;align-items:center;justify-content:center;margin-top:-28px}
.quick-label{margin-top:26px;color:#fff;font-size:17px;font-weight:600;text-align:center;line-height:31px}

.market{left:199px;top:1534px;width:802px;border-collapse:collapse;table-layout:fixed}
.market th{background:var(--dark);color:#fff;height:55px;font-size:16px;font-weight:600}
.market td{background:var(--cell);border:1px solid var(--cell-line);height:48px;text-align:center;font-size:16px;color:#5d6165}
.market td.row-label{text-align:left;padding-left:24px;color:#6f7378}
.market tr.trend td{height:141px}
.trend-cell{display:flex;flex-direction:column;align-items:center;gap:12px}
.trend-cell span{color:var(--teal);font-size:15px;font-weight:500}

.listing-bar{left:199px;top:2065px;width:802px;height:58px;background:var(--blue);color:#fff;font-size:22px;font-weight:500;letter-spacing:.5px;padding:15px 28px}
.listing-panel{left:199px;top:2123px;width:802px;height:454px;background:var(--panel)}
.listing-address{left:233px;top:2167px;font-size:18px;line-height:36px;color:#55595d}
.listing-price{left:233px;top:2280px;font-size:33px;color:var(--blue);font-weight:500}
.listing-facts{left:233px;top:2328px;font-size:18px;line-height:34px;color:#55595d}
.listing-more{left:233px;top:2484px;font-size:18px;font-weight:600;color:#3e4145;border-bottom:1px solid #8a8d90;padding-bottom:1px}
.listing-chart{left:493px;top:2180px}

.news{left:199px;top:2624px;width:802px;height:565px;background:var(--teal)}
.news-title{left:199px;top:2668px;width:802px;text-align:center;font-size:31px;color:#fff;font-weight:500}
.news-video{left:246px;top:2753px;width:700px;height:389px;
  background:linear-gradient(135deg,#0f2438 0%,#22496a 45%,#3a6f92 70%,#0d1b2a 100%)}

.events-title{left:225px;top:3243px;font-size:22px;font-weight:500;letter-spacing:.5px}
.events-rule{left:225px;top:3287px;width:748px}
.events-photo{left:225px;top:3322px;width:745px;height:168px;
  background:linear-gradient(180deg,#4f96d6 0%,#8cc0ea 45%,#b8a892 62%,#7d8a6a 82%,#5c6e4a 100%)}
.events-copy{left:225px;top:3513px;width:748px}

.social{left:199px;top:3673px;width:802px;height:97px;background:var(--band);display:flex;align-items:center;padding:0 28px 0 32px}
.social-label{font-size:21px;color:#7d8286;letter-spacing:.5px;flex:1}
.social-squares{display:flex;gap:20px}
.social-squares span{width:42px;height:42px;background:#1c9ad6;display:block}

.footer{left:0;top:3772px;width:1200px;height:150px;background:#2e2f30;text-align:center;padding-top:26px;font-size:14px;line-height:33px;color:var(--footer-text)}
.footer .prefs{color:var(--blue)}
</style>
</head>
<body>

<div class="abs sent-date">Fri, Feb 21, 2014 at 6:52 AM</div>
<svg class="abs sent-toggle" viewBox="0 0 16 10"><path d="M2 2l6 6 6-6" fill="none" stroke="#555" stroke-width="2"/></svg>

<div class="abs sheet"></div>

<div class="abs hero" role="img" aria-label="Sunlit turquoise ocean surf rolling onto a sandy beach under a blue sky"></div>
<div class="abs brand-box"><div class="brand-name">Kestwin Shoreline Homes</div></div>
<div class="abs tagline">YOUR COASTAL CLOSERS</div>

<nav class="abs main-nav">
  <span>MARKET DATA</span><span>FEATURED LISTINGS</span><span>REAL ESTATE NEWS</span><span>OC EVENTS</span>
</nav>

<h2 class="abs section-title welcome-title">Welcome to High End Real Estate</h2>
<div class="abs rule welcome-rule"></div>
<p class="abs body-copy welcome-copy">Elementum pellentesque aliquet. Nullam sodales urna erat, vitae egestas nisl tincidunt et. Sed iaculis rhoncus dolor. Integer vel urna nec elit varius dapibus ac nec mi. Vestibulum at nulla nec nulla pharetra sollicitudin.</p>

<div class="abs letter"></div>
<div class="abs portrait" role="img" aria-label="Portrait of the agent in a grey suit"></div>
<h2 class="abs letter-title">JAN 2014 NEWSLETTER</h2>
<p class="abs letter-copy">Elementum pellentesque aliquet. Nullam sodales urna erat, vitae egestas nisl tincidunt et. Sed iaculis rhoncus dolor. Integer vel urna nec elit varius dapibus ac nec mi. Vestibulum at nulla nec nulla pharetra sollicitudin.</p>
<div class="abs letter-name">REID HALLOWAY</div>
<div class="abs letter-mail">Email Me</div>

<h3 class="abs links-title">Find below quick links to each segment of our newsletter:</h3>
<div class="abs rule links-rule"></div>

<div class="abs quick-links">
  <div class="quick-link">
    <div class="quick-icon"><svg width="40" height="40" viewBox="0 0 40 40"><path d="M20 6L4 20h5v14h9v-9h4v9h9V20h5z" fill="#33a6d7"/></svg></div>
    <div class="quick-label">Real Estate<br>Market Data</div>
  </div>
  <div class="quick-link">
    <div class="quick-icon"><svg width="40" height="40" viewBox="0 0 40 40"><rect x="10" y="5" width="20" height="31" fill="#33a6d7"/><g fill="#fff"><rect x="14" y="10" width="4" height="4"/><rect x="22" y="10" width="4" height="4"/><rect x="14" y="17" width="4" height="4"/><rect x="22" y="17" width="4" height="4"/><rect x="14" y="24" width="4" height="4"/><rect x="22" y="24" width="4" height="4"/><rect x="18" y="30" width="4" height="6"/></g></svg></div>
    <div class="quick-label">Featured Property<br>Listings</div>
  </div>
  <div class="quick-link">
    <div class="quick-icon"><svg width="40" height="40" viewBox="0 0 40 40"><path d="M8 16h6l14-8v24l-14-8H8z" fill="#33a6d7"/><path d="M12 24l3 9h4l-3-9z" fill="#33a6d7"/></svg></div>
    <div class="quick-label">News You<br>Can Use</div>
  </div>
  <div class="quick-link">
    <div class="quick-icon"><svg width="40" height="40" viewBox="0 0 40 40"><rect x="7" y="9" width="26" height="25" rx="2" fill="none" stroke="#33a6d7" stroke-width="3"/><rect x="7" y="9" width="26" height="7" fill="#33a6d7"/><rect x="12" y="5" width="3" height="7" fill="#33a6d7"/><rect x="25" y="5" width="3" height="7" fill="#33a6d7"/><g fill="#33a6d7"><rect x="12" y="20" width="4" height="4"/><rect x="18" y="20" width="4" height="4"/><rect x="24" y="20" width="4" height="4"/><rect x="12" y="26" width="4" height="4"/><rect x="18" y="26" width="4" height="4"/></g></svg></div>
    <div class="quick-label">Oc Community<br>Events</div>
  </div>
</div>

<table class="abs market">
  <colgroup><col style="width:219px"><col><col><col><col><col></colgroup>
  <thead><tr><th>Zip Code:</th><th>92677</th><th>92651</th><th>92672</th><th>92673</th><th>92629</th></tr></thead>
  <tbody>
    <tr><td class="row-label">Monthly Units Sold</td><td>115</td><td>116</td><td>117</td><td>118</td><td>119</td></tr>
    <tr><td class="row-label">Avg. Sold Price</td><td>$583K</td><td>$583K</td><td>$583K</td><td>$583K</td><td>$583K</td></tr>
    <tr><td class="row-label">Sold % of Orig List $</td><td>95.5%</td><td>95.5%</td><td>95.5%</td><td>95.5%</td><td>95.5%</td></tr>
    <tr><td class="row-label">Current Units Listed</td><td>122</td><td>122</td><td>122</td><td>122</td><td>122</td></tr>
    <tr><td class="row-label">Avg. List Price</td><td>$1,415K</td><td>$1,415K</td><td>$1,415K</td><td>$1,415K</td><td>$1,415K</td></tr>
    <tr><td class="row-label">Avg. Days on Market</td><td>83</td><td>83</td><td>83</td><td>83</td><td>83</td></tr>
    <tr class="trend"><td class="row-label">Historical Trends</td>
      <td><div class="trend-cell"><svg width="44" height="44" viewBox="0 0 44 44"><circle cx="22" cy="22" r="18" fill="none" stroke="#00a990" stroke-width="4"/><rect x="14" y="22" width="4" height="9" fill="#00a990"/><rect x="20" y="16" width="4" height="15" fill="#00a990"/><rect x="26" y="12" width="4" height="19" fill="#00a990"/></svg><span>See Chart</span></div></td>
      <td><div class="trend-cell"><svg width="44" height="44" viewBox="0 0 44 44"><circle cx="22" cy="22" r="18" fill="none" stroke="#00a990" stroke-width="4"/><rect x="14" y="22" width="4" height="9" fill="#00a990"/><rect x="20" y="16" width="4" height="15" fill="#00a990"/><rect x="26" y="12" width="4" height="19" fill="#00a990"/></svg><span>See Chart</span></div></td>
      <td><div class="trend-cell"><svg width="44" height="44" viewBox="0 0 44 44"><circle cx="22" cy="22" r="18" fill="none" stroke="#00a990" stroke-width="4"/><rect x="14" y="22" width="4" height="9" fill="#00a990"/><rect x="20" y="16" width="4" height="15" fill="#00a990"/><rect x="26" y="12" width="4" height="19" fill="#00a990"/></svg><span>See Chart</span></div></td>
      <td><div class="trend-cell"><svg width="44" height="44" viewBox="0 0 44 44"><circle cx="22" cy="22" r="18" fill="none" stroke="#00a990" stroke-width="4"/><rect x="14" y="22" width="4" height="9" fill="#00a990"/><rect x="20" y="16" width="4" height="15" fill="#00a990"/><rect x="26" y="12" width="4" height="19" fill="#00a990"/></svg><span>See Chart</span></div></td>
      <td><div class="trend-cell"><svg width="44" height="44" viewBox="0 0 44 44"><circle cx="22" cy="22" r="18" fill="none" stroke="#00a990" stroke-width="4"/><rect x="14" y="22" width="4" height="9" fill="#00a990"/><rect x="20" y="16" width="4" height="15" fill="#00a990"/><rect x="26" y="12" width="4" height="19" fill="#00a990"/></svg><span>See Chart</span></div></td>
    </tr>
  </tbody>
</table>

<div class="abs listing-bar">FEATURED LISTINGS</div>
<div class="abs listing-panel"></div>
<div class="abs listing-address">12 Tidewater Crest<br>Laguna Niguel,<br>CA 92677</div>
<div class="abs listing-price">$489,900</div>
<div class="abs listing-facts">Bedrooms: 2 beds<br>Bathrooms: 2 full<br>Sq. Footage: 1,200<br>MLS# OC13245720</div>
<div class="abs listing-more">View Listing Details</div>

<svg class="abs listing-chart" width="485" height="300" viewBox="0 0 485 300" font-family="Figtree, Arial, sans-serif" font-size="12" fill="#555">
  <g text-anchor="end">
    <text x="28" y="266">0</text><text x="28" y="238">100</text><text x="28" y="211">200</text>
    <text x="28" y="183">300</text><text x="28" y="156">400</text><text x="28" y="128">500</text>
    <text x="28" y="101">600</text><text x="28" y="73">700</text><text x="28" y="46">800</text>
    <text x="28" y="18">900</text>
  </g>
  <line x1="38" y1="262" x2="480" y2="262" stroke="#c8cbce"/>
  <g>
    <rect x="49" y="171" width="24" height="91" fill="var(--bar-top)"/><rect x="49" y="196" width="24" height="66" fill="var(--bar)"/>
    <rect x="89" y="165.5" width="24" height="96.5" fill="var(--bar-top)"/><rect x="89" y="179" width="24" height="83" fill="var(--bar)"/>
    <rect x="129" y="135" width="24" height="127" fill="var(--bar-top)"/><rect x="129" y="138" width="24" height="124" fill="var(--bar)"/>
    <rect x="169" y="91" width="24" height="171" fill="var(--bar-top)"/><rect x="169" y="99" width="24" height="163" fill="var(--bar)"/>
    <rect x="209" y="42" width="24" height="220" fill="var(--bar-top)"/><rect x="209" y="53" width="24" height="209" fill="var(--bar)"/>
    <rect x="249" y="58" width="24" height="204" fill="var(--bar-top)"/><rect x="249" y="86" width="24" height="176" fill="var(--bar)"/>
    <rect x="289" y="86" width="24" height="176" fill="var(--bar-top)"/><rect x="289" y="102" width="24" height="160" fill="var(--bar)"/>
    <rect x="329" y="132" width="24" height="130" fill="var(--bar-top)"/><rect x="329" y="177" width="24" height="85" fill="var(--bar)"/>
    <rect x="369" y="99" width="24" height="163" fill="var(--bar-top)"/><rect x="369" y="108" width="24" height="154" fill="var(--bar)"/>
    <rect x="409" y="77" width="24" height="185" fill="var(--bar-top)"/><rect x="409" y="86" width="24" height="176" fill="var(--bar)"/>
    <rect x="449" y="66" width="24" height="196" fill="var(--bar-top)"/><rect x="449" y="72" width="24" height="190" fill="var(--bar)"/>
  </g>
  <g text-anchor="middle">
    <text x="61" y="284">oct</text><text x="101" y="284">nov</text><text x="141" y="284">dec</text>
    <text x="181" y="284">jan</text><text x="221" y="284">feb</text><text x="261" y="284">mar</text>
    <text x="301" y="284">apr</text><text x="341" y="284">may</text><text x="381" y="284">june</text>
    <text x="421" y="284">july</text><text x="461" y="284">aug</text>
  </g>
</svg>

<div class="abs news"></div>
<h2 class="abs news-title">News You Can Use</h2>
<div class="abs news-video" role="img" aria-label="Embedded market news video showing a treasury yield chart"></div>

<h2 class="abs events-title">UPCOMING EVENTS</h2>
<div class="abs rule events-rule"></div>
<div class="abs events-photo" role="img" aria-label="Row of suburban two-storey homes under a blue sky"></div>
<p class="abs body-copy events-copy">Elementum pellentesque aliquet. Nullam sodales urna erat, vitae egestas nisl tincidunt et. Sed iaculis rhoncus dolor. Integer vel urna nec elit varius dapibus ac nec mi. Vestibulum at nulla nec nulla pharetra sollicitudin.</p>

<div class="abs social">
  <div class="social-label">Stay In Touch With Us:</div>
  <div class="social-squares"><span></span><span></span><span></span><span></span><span></span></div>
</div>

<footer class="abs footer">
  <div>Copyright © 2014 KestwinShorelineHomes, All rights reserved.</div>
  <div>Our mailing address is: KestwinShorelineHomes 48 Harborview Lane Seacliff Point,CA92600</div>
  <div class="prefs">unsubscribe from this list | update subscription preferences.</div>
</footer>

</body>
</html>
```